Professional Website Design to match new logo for Medical Legal Company

We have rebranded our company and We want a professional but also dynamic web site design for a group of esteemed doctors that provide expert evaluation of an injured worker in a Workers Compensation case.
​
1. Our target market is both the attorneys who select our doctors and any doctors who would wish to join our group.

2. Notes for the Landing Page:
- We prefer a simpler, sleeker more modern look for the landing page.
- We want a simplified landing page with one image, three buttons highlighted in Content document.
- We want the main image to be black and white but it can be splashed with color.
-We think the landing page might be enhanced by add a dark blue or black as a primary color. Of course please feel free to try any color combination you think might work.
- We want "The Meridale Circle" in large letters and "Stewards of a fair and prompt outcome" in small lettering. We don't want icons on the buttons.
- Do not want more than the one picture at top of landing page.
- We do not want any pictures that include faces. Please eliminate or replace. They will not be chosen.
- For the landing page, instead of a second set of photos please experiment with using medical symbols and legal symbols.
​
3. New Company Name: The Meridale Circle
New logo is uploaded bronze and grey/silver will be colors although we are still tweaking the colors for more metallic feel. Want simple not busy.

4. The overall Web page design needs to have some website design effect (e,g image rollover, scrolling effect, hover effect etc).

5. Please follow the attached word document file for the page content of the 4 web pages. Do not mix it up.

Previous company website: www.clinicjuristpanel.example (we wish to convert some of the content from this website to the new brand). Competitor website that we like: www.docboardly.example

Target Market(s)

Professional Elite. Attorneys and Doctors

Industry/Entity Type

Medical Legal

Coding

Coded - Design and coding required

Number of Pages Required

5+ page

Font styles to use
Other font styles liked:
• Helvetica or maybe font that matches logo. We are open

Colors

Designer to choose colors to be used in the design.

Requirements
Must have
• I can't locate on color scale but we want Bronze and Silver/Grey from logo. Additional colors can be added. Various shades of grey
Nice to have
• Black and white photos, simple elegant design
Should not have
• Images with faces of unknown people

```html
<!DOCTYPE html>
<html lang="en">
<head>
<meta charset="utf-8">
<title>The Meridale Circle</title>
<link href="https://fonts.googleapis.com/css2?family=Roboto:wght@400;500;700;900&display=swap" rel="stylesheet">
<style>
  :root{
    --navy:#0e0b52;
    --navy-deep:#0b0845;
    --navy-band:#1c1867;
    --bronze:#b07048;
    --silver:#9a9aa6;
    --ink:#0a0a0a;
    --grey-text:#5a5a5a;
    --panel:#f1f0f5;
    --white:#ffffff;
  }
  *{margin:0;padding:0;box-sizing:border-box}
  html,body{width:843px;height:1200px;overflow:hidden;background:var(--white)}
  body{font-family:"Roboto",Arial,sans-serif;position:relative}

  /* header */
  .site-header{position:absolute;left:0;top:0;width:843px;height:56px;background:var(--navy)}
  .brand{position:absolute;display:flex;align-items:center;gap:6px;color:#c9c9d4;font-weight:700;font-size:13px;letter-spacing:.8px;white-space:nowrap}
  .brand-header{left:101px;top:16px}
  .brand-footer{left:107px;top:112px}
  .brand-dot{width:14px;height:14px;border-radius:50%;background:var(--bronze)}
  .main-nav a{position:absolute;top:21px;color:var(--white);font-size:9.6px;font-weight:500;text-decoration:none;white-space:nowrap}

  /* hero */
  .hero{position:absolute;left:0;top:56px;width:843px;height:426px;
    background:linear-gradient(90deg,#e7e6f0 0%,#e4e3ed 52%,#cfced8 68%,#b4b3bd 84%,#a4a3ad 100%)}
  .hero-title{position:absolute;left:99px;top:204px;font-size:28.5px;font-weight:700;color:var(--ink);letter-spacing:.3px;white-space:nowrap}
  .hero-tagline{position:absolute;left:99px;top:247px;font-size:10.8px;color:var(--ink);white-space:nowrap}
  .pill{position:absolute;top:292px;height:36px;border-radius:18px;display:flex;align-items:center;justify-content:center;
    color:var(--white);font-size:10.8px;font-weight:700;white-space:nowrap;text-decoration:none}
  .pill-stake{left:99px;width:128px;background:var(--bronze)}
  .pill-qme{left:242px;width:136px;background:var(--ink)}
  .pill-member{left:392px;width:154px;background:var(--navy)}

  /* welcome */
  .welcome-band{position:absolute;left:0;top:482px;width:260px;height:352px;background:var(--navy-band)}
  .welcome-card{position:absolute;left:96px;top:541px;width:327px;height:235px;background:var(--white);border-radius:4px}
  .symbol-panel{position:absolute;left:101px;top:546px;width:321px;height:224px;background:var(--panel);
    display:flex;align-items:center;justify-content:center;gap:44px}
  .welcome-kicker{position:absolute;left:463px;top:592px;font-size:10.8px;color:var(--bronze)}
  .welcome-title{position:absolute;left:463px;top:609px;font-size:22.5px;font-weight:700;color:var(--ink);white-space:nowrap}
  .welcome-text{position:absolute;left:469px;top:651px;width:272px;font-size:9px;line-height:18px;color:var(--grey-text);text-align:justify}

  /* newsletter */
  .newsletter{position:absolute;left:0;top:834px;width:843px;height:102px;background:var(--bronze)}
  .newsletter-title{position:absolute;left:100px;top:36px;font-size:22.5px;font-weight:700;color:var(--white);white-space:nowrap}
  .download-btn{position:absolute;left:615px;top:35px;width:126px;height:32px;border-radius:16px;background:var(--navy);
    color:var(--white);font-size:9.5px;font-weight:700;display:flex;align-items:center;justify-content:center;gap:5px}

  /* footer */
  .site-footer{position:absolute;left:0;top:936px;width:843px;height:264px;background:var(--navy-deep)}
  .footer-rule{position:absolute;width:1px;top:48px;height:160px;background:#3a3780}
  .footer-rule::before{content:"";position:absolute;left:-1px;top:0;width:3px;height:30px;background:var(--bronze)}
  .footer-heading{position:absolute;top:47px;font-size:10.2px;font-weight:500;color:var(--white)}
  .quick-links{position:absolute;left:378px;top:76px;list-style:none}
  .quick-links li{font-size:9px;line-height:16.9px;color:var(--white)}
  .contact-item{position:absolute;left:569px;display:flex;gap:8px;color:var(--white);font-size:9.6px;font-weight:500;line-height:17px}
  .contact-item svg{flex:none;margin-top:2px}
  .footer-divider{position:absolute;left:101px;top:208px;width:641px;height:1px;background:#3a3780}
  .copyright{position:absolute;left:101px;top:228px;font-size:9px;color:var(--white)}
  .social{position:absolute;top:226px;width:19px;height:19px;border:1px solid var(--white);border-radius:50%}
  .legal{position:absolute;left:603px;top:228px;font-size:9px;color:var(--white);white-space:nowrap}
  .legal-sep{margin:0 9px}
</style>
</head>
<body>

<header class="site-header">
  <div class="brand brand-header"><span class="brand-dot"></span>THE MERIDALE CIRCLE</div>
  <nav class="main-nav">
    <a style="left:359px">Home</a>
    <a style="left:404px">Physicians</a>
    <a style="left:470px">Stakeholder</a>
    <a style="left:542px">Meridale Gives Back</a>
    <a style="left:653px">Blog</a>
    <a style="left:691px">Contact Us</a>
  </nav>
</header>

<section class="hero" role="img" aria-label="Black and white photo of a physician in a white coat holding a clipboard in a bright clinic"></section>
<h1 class="hero-title">THE MERIDALE CIRCLE</h1>
<p class="hero-tagline">Stewards of a fair and prompt outcome</p>
<a class="pill pill-stake">Stakeholders</a>
<a class="pill pill-qme">QME Physicians</a>
<a class="pill pill-member">Member Physicians</a>

<div class="welcome-band"></div>
<div class="welcome-card"></div>
<div class="symbol-panel" aria-label="Medical and legal symbols">
  <svg width="80" height="80" viewBox="0 0 80 80" aria-hidden="true">
    <path d="M30 6h20v24h24v20H50v24H30V50H6V30h24z" fill="none" stroke="#0e0b52" stroke-width="4"/>
  </svg>
  <svg width="96" height="84" viewBox="0 0 96 84" aria-hidden="true">
    <g stroke="#b07048" stroke-width="3" fill="none" stroke-linecap="round">
      <line x1="48" y1="8" x2="48" y2="74"/>
      <line x1="14" y1="18" x2="82" y2="18"/>
      <line x1="30" y1="76" x2="66" y2="76"/>
      <path d="M14 18L4 44M14 18l10 26M4 44a10 6 0 0 0 20 0z"/>
      <path d="M82 18L72 44M82 18l10 26M72 44a10 6 0 0 0 20 0z"/>
    </g>
    <circle cx="48" cy="8" r="4" fill="#b07048"/>
  </svg>
</div>
<p class="welcome-kicker">Welcome To</p>
<h2 class="welcome-title">THE MERIDALE CIRCLE</h2>
<p class="welcome-text">The Meridale Circle is a leader in Qualified Medical Evaluations and SIBTF cases in the State of California. Our doctors are dedicated to facilitating settlements through rapid, objective and well researched Expert Medical Opinions</p>

<section class="newsletter">
  <h2 class="newsletter-title">MOST RECENT NEWSLETTER</h2>
  <a class="download-btn">
    <svg width="9" height="9" viewBox="0 0 10 10"><path d="M5 0v6M2.5 3.5L5 6l2.5-2.5" stroke="#fff" stroke-width="1.6" fill="none"/><rect x="0" y="8" width="10" height="2" fill="#fff"/></svg>
    DOWNLOAD
  </a>
</section>

<footer class="site-footer">
  <div class="brand brand-footer"><span class="brand-dot"></span>THE MERIDALE CIRCLE</div>
  <div class="footer-rule" style="left:309px"></div>
  <div class="footer-rule" style="left:528px"></div>

  <h3 class="footer-heading" style="left:378px">QUICK LINKS</h3>
  <ul class="quick-links">
    <li>Home</li><li>Physicians</li><li>Stakeholder</li><li>Meridale Gives Back</li><li>Blog</li><li>Contact Us</li>
  </ul>

  <h3 class="footer-heading" style="left:569px">CONTACT INFO</h3>
  <div class="contact-item" style="top:72px">
    <svg width="13" height="13" viewBox="0 0 12 14"><path d="M6 0a4.5 4.5 0 0 0-4.5 4.5C1.5 8 6 14 6 14s4.5-6 4.5-9.5A4.5 4.5 0 0 0 6 0z" fill="#b07048"/><circle cx="6" cy="4.6" r="1.7" fill="#0b0845"/></svg>
    <span>2180 Corvell Avenue, 4th Floor<br>Brenmoor, CA 90412</span>
  </div>
  <div class="contact-item" style="top:114px">
    <svg width="13" height="10" viewBox="0 0 13 10"><rect x=".5" y=".5" width="12" height="9" fill="none" stroke="#b07048"/><path d="M.5.5l6 5 6-5" stroke="#b07048" fill="none"/></svg>
    <span>hello@meridalecircle.example</span>
  </div>
  <div class="contact-item" style="top:141px">
    <svg width="13" height="13" viewBox="0 0 12 12"><path d="M2.5 1l2 2.3-1.2 1.5c.8 1.6 2.1 2.9 3.7 3.7l1.5-1.2L10.9 9.4 9.6 11C5 10.6 1.3 6.9 1 2.3z" fill="#b07048"/></svg>
    <span>(800) 555-0142</span>
  </div>
  <div class="contact-item" style="top:167px">
    <svg width="13" height="13" viewBox="0 0 12 12"><rect x="0" y="4" width="3" height="8" fill="#b07048"/><rect x="4" y="3" width="8" height="9" fill="#b07048"/><rect x="5" y="0" width="6" height="3" fill="#b07048"/></svg>
    <span>(310) 555-0187</span>
  </div>

  <div class="footer-divider"></div>
  <p class="copyright">Copyright The Meridale Circle © 2024. All Rights Reserved.</p>
  <span class="social" style="left:446px"></span>
  <span class="social" style="left:471px"></span>
  <span class="social" style="left:495px"></span>
  <p class="legal">Privacy Policy<span class="legal-sep">|</span>Terms Of Use</p>
</footer>

</body>
</html>
```